Advertisement Design for weight loss

i need an ad design about: Abdominal, belly, tightening & slimming, weight loss,
4 days max need it by 11th april Friday .

actually i need 3 design about the same idea,

so you post your design and if i like it you`r a winner, simple`s that !

important: all girls in your design must not be almost naked please :)
you can put some shorts, shirts, jeans etc

i`ll add the text by my self, just put editable text layer that`s all .

```html
<!DOCTYPE html>
<html lang="en">
<head>
<meta charset="utf-8">
<title>Slimming Advertisement</title>
<link href="https://fonts.googleapis.com/css2?family=Arimo:wght@700&display=swap" rel="stylesheet">
<style>
  :root {
    --page-bg: #ffffff;
    --panel-top: #44a3dd;
    --panel-bottom: #1d5d9e;
    --stripe: rgba(255, 255, 255, 0.55);
    --text-light: #ffffff;
    --frame: #ffffff;
    --photo-bg: #d9d9db;
    --photo-skin: #e3c3aa;
    --photo-cloth: #f0c6d8;
  }
  html, body {
    margin: 0;
    padding: 0;
    width: 852px;
    height: 1200px;
    overflow: hidden;
    background: var(--page-bg);
  }
  .canvas {
    position: relative;
    width: 852px;
    height: 1200px;
    font-family: "Arimo", Arial, sans-serif;
    font-weight: 700;
    color: var(--text-light);
  }
  .panel {
    position: absolute;
    left: 28px;
    top: 27px;
    width: 793px;
    height: 1147px;
    border-radius: 38px;
    overflow: hidden;
    background: linear-gradient(180deg, var(--panel-top) 0%, var(--panel-bottom) 100%);
  }
  .panel-stripes {
    position: absolute;
    inset: 0;
    background: repeating-linear-gradient(
      45deg,
      transparent 0px,
      transparent 22px,
      var(--stripe) 22px,
      var(--stripe) 24px
    );
  }
  .logo-name {
    position: absolute;
    left: 55px;
    top: 50px;
    margin: 0;
    font-size: 53px;
    line-height: 1;
    letter-spacing: 0.5px;
  }
  .copy {
    position: absolute;
    margin: 0;
    text-transform: uppercase;
  }
  .copy-intro {
    left: 430px;
    top: 96px;
    font-size: 17px;
    line-height: 24.5px;
  }
  .copy-middle {
    left: 335px;
    top: 782px;
    font-size: 24.5px;
    line-height: 34px;
  }
  .copy-bottom {
    left: 61px;
    top: 989px;
    font-size: 24.5px;
    line-height: 34px;
  }
  .photo-frame {
    position: absolute;
    left: 61px;
    top: 240px;
    width: 731px;
    height: 489px;
    background: var(--frame);
    box-sizing: border-box;
    padding: 8px;
  }
  .photo {
    width: 100%;
    height: 100%;
    background:
      linear-gradient(180deg, transparent 0%, transparent 74%, var(--photo-cloth) 74%, var(--photo-cloth) 100%),
      linear-gradient(90deg, var(--photo-skin) 0%, var(--photo-skin) 84%, var(--photo-bg) 84%, var(--photo-bg) 100%);
  }
</style>
</head>
<body>
  <main class="canvas">
    <section class="panel">
      <div class="panel-stripes"></div>
    </section>

    <h1 class="logo-name">LOGO HERE</h1>

    <p class="copy copy-intro">
      Lorem ipsum dolor sit amet,<br>
      consectetuer adipiscing<br>
      elit, sed diam nonummy nibh<br>
      euismod tincidunt
    </p>

    <figure class="photo-frame" style="margin:0;">
      <div class="photo" role="img" aria-label="Photo of a woman's bare midriff wearing pink shorts, measuring her waist with a yellow tape measure"></div>
    </figure>

    <p class="copy copy-middle">
      Lorem ipsum dolor sit amet,<br>
      consectetuer adipiscing<br>
      elit, sed diam nonummy nibh<br>
      euismod tincidunt
    </p>

    <p class="copy copy-bottom">
      Lorem ipsum dolor sit amet,<br>
      consectetuer adipiscing<br>
      elit, sed diam nonummy nibh<br>
      euismod tincidunt
    </p>
  </main>
</body>
</html>
```